Business Card + Stationery Design for a Craft Beer Bar

Mr. Tolvek's is a taproom sport bar that contains in its menu beers from different places around the world. What we offer differently is the experience that you can get inside our location, ambient music with rock from the 80s to 90s, projection with the sports of the moment, board games and private events.

Target Market(s)

Young people, Mid and High Class

Industry/Entity Type

Business

Font styles to use
Serif
Sans Serif

Colors
fee18a

Requirements
Must have
• Name, Title, Contact Details, Website
Nice to have
• Mail Signature
Should not have
• n/a

```html
<!DOCTYPE html>
<html lang="en">
<head>
<meta charset="utf-8">
<title>Mr. Tolvek's Taproom – Business Card</title>
<link rel="stylesheet" href="https://fonts.googleapis.com/css2?family=Oswald:wght@600&family=Josefin+Sans:wght@400;600&display=swap">
<style>
  :root {
    --backdrop: #2e2622;
    --card: #141414;
    --card-edge: #1d1d1d;
    --silver: #cfcfcf;
    --gloss: #050505;
    --gold: #fee18a;
    --white: #f2f2f2;
  }
  * { margin: 0; padding: 0; box-sizing: border-box; }
  html, body { width: 1200px; height: 715px; overflow: hidden; }
  body {
    background: var(--backdrop);
    display: flex;
    align-items: center;
    justify-content: center;
    gap: 80px;
    font-family: "Josefin Sans", sans-serif;
  }
  .card {
    position: relative;
    width: 330px;
    height: 578px;
    background: var(--card);
    border: 1px solid var(--card-edge);
    border-radius: 4px;
    box-shadow: 0 14px 34px rgba(0,0,0,.45);
  }
  .brand {
    position: absolute;
    left: 0; right: 0;
    display: flex;
    flex-direction: column;
    align-items: center;
    gap: 18px;
  }
  .brand-mark {
    width: 64px;
    height: 64px;
    border-radius: 50%;
  }
  .brand-name {
    font-family: "Josefin Sans", sans-serif;
    font-weight: 600;
    font-size: 30px;
    line-height: 1;
    letter-spacing: .04em;
  }
  .card-front .brand { top: 210px; }
  .card-front .brand-mark { background: var(--silver); }
  .card-front .brand-name { color: var(--silver); }
  .card-back .brand { top: 62px; }
  .card-back .brand-mark { background: var(--gloss); }
  .card-back .brand-name { color: var(--gloss); }
  .contact {
    position: absolute;
    left: 36px;
    bottom: 56px;
    color: var(--white);
    font-size: 12px;
    letter-spacing: .12em;
    text-transform: uppercase;
    line-height: 1.8;
  }
  .contact .person {
    font-family: "Oswald", sans-serif;
    font-weight: 600;
    font-size: 26px;
    color: var(--gold);
    letter-spacing: .04em;
    line-height: 1.1;
  }
  .contact .rule {
    width: 34px;
    height: 2px;
    background: var(--gold);
    margin: 10px 0 8px;
  }
  .contact .label { color: var(--gold); }
</style>
</head>
<body>
  <section class="card card-front" aria-label="Card front">
    <div class="brand">
      <div class="brand-mark" role="img" aria-label="Taproom emblem"></div>
      <div class="brand-name">MR. TOLVEK'S</div>
    </div>
  </section>

  <section class="card card-back" aria-label="Card back">
    <div class="brand">
      <div class="brand-mark" role="img" aria-label="Taproom emblem"></div>
      <div class="brand-name">MR. TOLVEK'S</div>
    </div>
    <div class="contact">
      <div class="person">MR. TOLVEK</div>
      <div class="rule"></div>
      <div><span class="label">Phone:</span> (123) 555-0147</div>
      <div><span class="label">Email:</span> info@mrtolveks.com</div>
      <div><span class="label">Web:</span> www.mrtolveks.com</div>
      <div class="rule"></div>
      <div>1187 Marlow Street</div>
      <div>Dalton, AL 35900</div>
    </div>
  </section>
</body>
</html>
```